Mabel's Fitness Business Cards

I would like my business cards to look expensive and sophisticated using my logo and the information below.

FRONT
Mabel’s Fitness logo

Tag line Become your happiest, healthiest and strongest self

Mabel Quint Harlow
Personal Trainer

e. mabel@mabelsfitstudio.example

t. 0781530462

w. www.mabelsfitstudio.example

```html
<!DOCTYPE html>
<html lang="en">
<head>
<meta charset="utf-8">
<title>Mabel's Fitness Business Cards</title>
<link rel="stylesheet" href="https://fonts.googleapis.com/css2?family=Josefin+Sans:wght@300;400;600&display=swap">
<style>
  :root {
    --backdrop: #1a1b1b;
    --card-white: #ffffff;
    --teal: #6bb5bf;
    --cocoa: #675a55;
    --taupe: #a39792;
    --ink: #5e5350;
  }
  * { box-sizing: border-box; margin: 0; padding: 0; }
  html, body {
    width: 1200px; height: 1000px; overflow: hidden;
    background: var(--backdrop);
    font-family: "Josefin Sans", "Helvetica Neue", Arial, sans-serif;
  }
  .stage { position: relative; width: 1200px; height: 1000px; }
  .card {
    position: absolute; width: 600px; height: 343px;
    border-radius: 30px; overflow: hidden;
  }
  /* Front card */
  .card-front { left: 440px; top: 170px; background: var(--card-white); }
  .brand {
    position: absolute; left: 0; right: 0; top: 105px;
    display: flex; flex-direction: column; align-items: center; gap: 18px;
  }
  .brand-dot {
    width: 54px; height: 54px; border-radius: 50%;
    border: 3px solid var(--teal);
  }
  .brand-name {
    color: var(--teal); font-weight: 400; font-size: 30px;
    letter-spacing: 6px; text-transform: uppercase; white-space: nowrap;
  }
  .tagline {
    position: absolute; left: 0; right: 0; bottom: 34px;
    text-align: center; color: var(--ink); font-size: 19px; font-weight: 400;
  }
  /* Back card */
  .card-back { left: 200px; top: 520px; background: var(--teal); }
  .card-back svg.shapes { position: absolute; inset: 0; }
  .holder { position: absolute; left: 32px; top: 32px; white-space: nowrap; }
  .holder-name { color: #fff; font-size: 24px; font-weight: 600; letter-spacing: .5px; }
  .holder-role { color: var(--cocoa); font-size: 19px; font-weight: 400; margin-top: 4px; }
  .contacts {
    position: absolute; left: 32px; top: 192px; list-style: none;
    display: flex; flex-direction: column; gap: 10px;
  }
  .contacts li {
    display: flex; align-items: center; gap: 10px; white-space: nowrap;
    color: #fff; font-size: 18px; font-weight: 300;
  }
  .contacts svg { width: 18px; height: 18px; flex: none; }
  .back-brand {
    position: absolute; left: 370px; top: 118px; width: 220px;
    display: flex; flex-direction: column; align-items: center; gap: 12px;
  }
  .back-brand .brand-dot { width: 40px; height: 40px; }
  .back-brand .brand-name { font-size: 18px; letter-spacing: 2px; }
</style>
</head>
<body>
<main class="stage">
  <section class="card card-front">
    <div class="brand">
      <span class="brand-dot"></span>
      <span class="brand-name">Mabel’s Fitness</span>
    </div>
    <p class="tagline">Become your happiest, healthiest and strongest self</p>
  </section>

  <section class="card card-back">
    <svg class="shapes" viewBox="0 0 600 343" aria-hidden="true">
      <circle cx="540" cy="160" r="200" fill="var(--card-white)"/>
      <circle cx="140" cy="440" r="300" fill="var(--cocoa)"/>
    </svg>
    <div class="holder">
      <p class="holder-name">Mabel Quint Harlow</p>
      <p class="holder-role">Personal Trainer</p>
    </div>
    <ul class="contacts">
      <li>
        <svg viewBox="0 0 24 24"><path d="M6.6 10.8a15 15 0 0 0 6.6 6.6l2.2-2.2c.3-.3.7-.4 1-.2 1.1.4 2.3.6 3.6.6.6 0 1 .4 1 1V20c0 .6-.4 1-1 1A17 17 0 0 1 3 4c0-.6.4-1 1-1h3.5c.6 0 1 .4 1 1 0 1.3.2 2.5.6 3.6.1.3 0 .7-.2 1z" fill="var(--teal)"/></svg>
        078 153 0462
      </li>
      <li>
        <svg viewBox="0 0 24 24"><rect x="2" y="5" width="20" height="14" rx="1" fill="var(--teal)"/><path d="M2.5 6l9.5 7 9.5-7" stroke="var(--cocoa)" stroke-width="1.6" fill="none"/></svg>
        mabel@mabelsfitstudio.example
      </li>
      <li>
        <svg viewBox="0 0 24 24" fill="none" stroke="var(--teal)" stroke-width="1.8"><circle cx="12" cy="12" r="9"/><path d="M3 12h18M12 3c3 3 3 15 0 18M12 3c-3 3-3 15 0 18"/></svg>
        mabelsfitstudio.example
      </li>
    </ul>
    <div class="back-brand">
      <span class="brand-dot"></span>
      <span class="brand-name">Mabel’s Fitness</span>
    </div>
  </section>
</main>
</body>
</html>
```